Brightfold Reach - B2B Demand Generation Website Project

We need a fully functional website for www.brightfoldreach-example.com. We are a B2B Demand Generation company, based in London, working with companies such as Halden, DWN, Vortan, Brelloway, Norvik generating them sales leads for their sales teams. We run this through digital marketing newsletter promotions and have a network of websites. Content syndication, data, demand generation, online marketing. Our logo has just been redone (attached) and we have a holding page already which i would like to use the style / colours. Our logo is bright and vibrant but i dont want the site to be a rainbow. We are expensive, classy, professorial, B2B, intelligent.

Home
About Us
Our Services
Prospero & QA Technology
Intent Data
Testimonials
Contact Us

Target Market(s)

B2B Marketers (Halden, Quorvane, Norvik, DWN, Vista Hub, Harrowby, Tremont Axis, Technology Companies, Data Companies, Marketing Teams, Cloudwick.

Industry/Entity Type

Marketing

Coding

Coded - Design and coding required

Number of Pages Required

5+ page

Font styles to use
Sans Serif

Requirements
Must have
• Home
About Us
Our Services
Prospero & QA Technology
Intent Data
Testimonials
Contact Us

Simple Pages.

Look classy, intelligent, data experts. I like the video homepages were the image moves at the top. Very soft animation.
Nice to have
• Websites i like:

https://www.dwn-example.com/
https://www.pulsegate-example.com/
https://www.lmsitecraft-example.co.uk/

Brightfold Reach - The Demand Generation Company
Should not have
• Pixelvault crap images

```html
<!DOCTYPE html>
<html lang="en">
<head>
<meta charset="utf-8">
<title>Brightfold Reach - The Demand Generation Company</title>
<link href="https://fonts.googleapis.com/css2?family=Montserrat:wght@400;500;600;700&display=swap" rel="stylesheet">
<style>
:root{
  --stage:#262626;
  --page:#ffffff;
  --navy:#0d4b8c;
  --red:#d7172a;
  --ink:#1f3f73;
  --muted:#9aa3b2;
  --line:#e3e6eb;
}
*{box-sizing:border-box;margin:0;padding:0}
html,body{width:1200px;height:1200px;overflow:hidden;background:var(--stage)}
body{font-family:'Montserrat',sans-serif}
.stage{position:absolute;left:0;top:0;width:1500px;height:1500px;transform:scale(.8);transform-origin:0 0}
.page{position:absolute;left:492px;top:46px;width:516px;height:1426px;background:var(--page);overflow:hidden}
.abs{position:absolute}

/* header */
.site-header{left:0;top:0;width:516px;height:29px;border-bottom:1px solid var(--line);background:#fff;z-index:3}
.brand{left:37px;top:7px;display:flex;align-items:center;gap:4px}
.brand-dot{width:13px;height:13px;border-radius:50%;border:2px solid var(--red)}
.brand-name{font-size:7px;font-weight:500;color:var(--navy);line-height:1}
.brand-sub{font-size:3px;color:var(--muted);display:block;margin-top:1px}
.main-nav{right:36px;top:10px;display:flex;gap:13px;font-size:4.3px;color:#7d8696}
.main-nav .active{color:var(--red);border-bottom:1px solid var(--red);padding-bottom:4px}

.hero-art{left:0;top:0;width:516px;height:560px}
.hero-title{left:141px;top:118px;width:200px;text-align:center;color:#fff;font-size:18px;font-weight:700;line-height:21px}

.bubble-text{left:70px;top:298px;width:182px;text-align:center;color:#fff;font-size:7.5px;line-height:12px}

/* services */
.services-title{left:79px;top:539px;font-size:12.5px;font-weight:600;color:var(--ink)}
.acc{left:220px;width:240px;font-size:5.6px;font-weight:600;color:var(--ink);border-bottom:1px solid var(--line);padding-bottom:5px}
.acc span{color:var(--red);margin-right:5px}
.acc-body{left:250px;top:529px;width:208px;font-size:4.2px;line-height:8.6px;color:var(--muted)}
.acc-icon{left:221px;top:530px}

.video{left:126px;top:630px;width:263px;height:152px}

/* testimonials */
.testimonials{left:0;top:817px;width:516px;height:178px;background:var(--navy)}
.section-head{left:0;top:17px;width:516px;text-align:center;color:#fff;font-size:10px;font-weight:700}
.card{background:#fff;text-align:center;padding-top:6px}
.card.faded{background:#b9cbe0}
.card.side{background:#dde6f1}
.quote{position:absolute;left:-4px;top:-12px;color:var(--red);font-size:22px;font-weight:700;line-height:1}
.avatar{width:20px;height:20px;border-radius:50%;margin:0 auto;background:linear-gradient(160deg,#6fb2d9,#c42530)}
.card h4{font-size:5.5px;font-weight:700;color:var(--ink);margin-top:5px}
.card small{display:block;font-size:3.6px;color:var(--red)}
.card p{font-size:3.4px;line-height:6px;color:var(--muted);padding:0 6px;margin-top:10px;text-align:left}

/* clients */
.client{font-size:12px;font-weight:700;color:var(--navy);width:80px;text-align:center}

/* stats */
.stats{left:0;top:1129px;width:516px;height:119px;background:linear-gradient(90deg,var(--navy) 0%,#3c3f84 55%,#b21e3b 100%)}
.stat{top:0;height:119px;text-align:center;color:#fff}
.stat + .stat{border-left:1px solid rgba(255,255,255,.35)}
.stat .label{margin-top:35px;font-size:7.5px;opacity:.9}
.stat .value{margin-top:28px;font-size:9px;font-weight:700}

/* footer */
.footer-mark{left:60px;top:1262px;width:26px;height:26px;border-radius:50%;border:3px solid var(--red);box-shadow:inset 0 0 0 3px var(--navy)}
.footer-about{left:57px;top:1302px;width:92px;font-size:4.6px;line-height:7.8px;color:var(--muted)}
.footer-nav{left:231px;top:1299px;list-style:none;font-size:6.3px;font-weight:600;color:var(--navy);line-height:11.6px}
.footer-contact{left:367px;top:1299px;font-size:4.6px;color:var(--muted);line-height:7.8px}
.footer-contact h5{font-size:6.3px;color:var(--navy);font-weight:600;margin-bottom:7px}
.footer-contact b{color:var(--ink);font-weight:600}
.copyright{left:0;top:1404px;width:516px;height:22px;background:var(--red);color:#fff;font-size:3.8px;text-align:center;line-height:22px}
</style>
</head>
<body>
<div class="stage">
<main class="page">

  <header class="site-header abs">
    <div class="brand abs">
      <span class="brand-dot"></span>
      <span class="brand-name">Brightfold Reach<span class="brand-sub">the demand generation company</span></span>
    </div>
    <nav class="main-nav abs">
      <span class="active">Home</span><span>About Us</span><span>Our Services</span><span>Prospero &amp; QA Technology</span><span>Intent Data</span><span>Testimonials</span><span>Contact Us</span>
    </nav>
  </header>

  <svg class="hero-art abs" viewBox="0 0 516 560">
    <defs>
      <linearGradient id="heroPhoto" x1="0" y1="0" x2="1" y2="1">
        <stop offset="0" stop-color="#e8e6e1"/><stop offset=".5" stop-color="#a9a49c"/><stop offset="1" stop-color="#6e6a66"/>
      </linearGradient>
      <radialGradient id="portrait" cx=".5" cy=".45" r=".6">
        <stop offset="0" stop-color="#d63a34"/><stop offset=".6" stop-color="#7fb8d6"/><stop offset="1" stop-color="#4e93bd"/>
      </radialGradient>
      <clipPath id="pageClip"><rect x="0" y="29" width="516" height="531"/></clipPath>
    </defs>
    <g clip-path="url(#pageClip)">
      <ellipse cx="262" cy="50" rx="318" ry="302" fill="url(#heroPhoto)" role="img" aria-label="Photo of a team meeting in a bright office with sticky notes on the wall"/>
    </g>
    <circle cx="304" cy="282" r="27" fill="var(--red)"/>
    <path d="M161 248a110 110 0 1 0 38 213l25 30-8-40a110 110 0 0 0-55-203z" fill="var(--navy)"/>
    <circle cx="37" cy="441" r="18" fill="var(--red)"/>
    <circle cx="407" cy="413" r="54" fill="url(#portrait)" role="img" aria-label="Portrait photo of a cheerful man in a red jumper"/>
  </svg>

  <h1 class="hero-title abs">We are a B2B Demand Generation company</h1>
  <p class="bubble-text abs">Brightfold Reach offers multi-channel demand generation services to publishers and technology vendors through our network of lead generation websites and native speaking telemarketing agents. Whether looking for MQL, ABM or BANT campaigns, Brightfold Reach can assist you in delivering your demand generation strategy and generate pipeline for your sales teams and/or channel partners.</p>

  <h2 class="services-title abs">Our Services</h2>
  <div class="acc abs" style="top:508px;border:none"><span>–</span>Marketing Qualified Leads (MQL)</div>
  <svg class="acc-icon abs" width="24" height="24" viewBox="0 0 24 24" fill="none" stroke="var(--red)" stroke-width=".8">
    <circle cx="12" cy="12" r="5"/><circle cx="12" cy="11" r="1.6"/><path d="M9.5 15a3 3 0 0 1 5 0"/>
    <circle cx="3" cy="4" r="1.6"/><circle cx="21" cy="4" r="1.6"/><circle cx="3" cy="20" r="1.6"/><circle cx="21" cy="20" r="1.6"/>
    <path d="M4.3 5.2 8.4 8.6M19.7 5.2l-4.1 3.4M4.3 18.8l4.1-3.4M19.7 18.8l-4.1-3.4"/>
  </svg>
  <p class="acc-body abs">A Marketing Qualified Lead (MQL) is a prospect that has expressed an interest in what your brand has to offer. An MQL has taken the first steps to becoming a customer and is ready to receive additional contact from your company.</p>
  <svg class="abs" style="left:440px;top:549px" width="14" height="6" viewBox="0 0 14 6"><path d="M0 3h13M10 .5 13 3l-3 2.5" stroke="var(--red)" stroke-width=".8" fill="none"/></svg>
  <div class="abs" style="left:220px;top:562px;width:240px;border-top:1px solid var(--line)"></div>
  <div class="acc abs" style="top:573px"><span>+</span>Account Based Marketing Leads (ABM)</div>
  <div class="acc abs" style="top:592px"><span>+</span>Sales Qualified Lead / BANT</div>

  <svg class="video abs" viewBox="0 0 263 152">
    <defs><linearGradient id="videoFill" x1="0" y1="0" x2="1" y2="1"><stop offset="0" stop-color="#4a5463"/><stop offset=".5" stop-color="#7b8796"/><stop offset="1" stop-color="#2b2f36"/></linearGradient></defs>
    <rect width="263" height="152" fill="url(#videoFill)" role="img" aria-label="Video still of a team working together around a laptop"/>
    <circle cx="132" cy="76" r="14" fill="#fff" opacity=".92"/>
    <path d="M128 69v14l11-7z" fill="var(--red)"/>
  </svg>

  <section class="testimonials abs">
    <h2 class="section-head abs">What Client Say</h2>
    <div class="card faded abs" style="left:56px;top:61px;width:67px;height:81px"><span class="quote">“</span><div class="avatar"></div><h4>SAM CARTER</h4><small>Founder</small><p>Clear leads, fast reporting, and a team that knows our market well.</p></div>
    <div class="card side abs" style="left:130px;top:56px;width:76px;height:93px"><span class="quote">“</span><div class="avatar"></div><h4>SAM CARTER</h4><small>Founder</small><p>Clear leads, fast reporting, and a team that knows our market well.</p></div>
    <div class="card abs" style="left:214px;top:49px;width:88px;height:108px"><span class="quote" style="font-size:28px;top:-14px">“</span><div class="avatar" style="width:26px;height:26px"></div><h4 style="font-size:6.5px">SAM CARTER</h4><small>Founder</small><p>Clear leads, fast reporting, and a team that knows our market well.</p></div>
    <div class="card side abs" style="left:310px;top:56px;width:76px;height:93px"><span class="quote">“</span><div class="avatar"></div><h4>SAM CARTER</h4><small>Founder</small><p>Clear leads, fast reporting, and a team that knows our market well.</p></div>
    <div class="card faded abs" style="left:393px;top:61px;width:66px;height:81px"><span class="quote">“</span><div class="avatar"></div><h4>SAM CARTER</h4><small>Founder</small><p>Clear leads, fast reporting, and a team that knows our market well.</p></div>
  </section>

  <div class="client abs" style="left:60px;top:1032px">Halden</div>
  <div class="client abs" style="left:142px;top:1032px">Norvik</div>
  <div class="client abs" style="left:220px;top:1032px">Tessaline</div>
  <div class="client abs" style="left:300px;top:1032px">Brackwater</div>
  <div class="client abs" style="left:382px;top:1032px">Ombrel</div>
  <div class="client abs" style="left:60px;top:1086px">Fenmoor</div>
  <div class="client abs" style="left:142px;top:1086px">Quillon</div>
  <div class="client abs" style="left:220px;top:1086px">Starrow</div>
  <div class="client abs" style="left:300px;top:1086px">Velden</div>

  <section class="stats abs">
    <div class="stat abs" style="left:0;width:184px"><p class="label">Downloads Per Month</p><p class="value">Ticker to 70,000+</p></div>
    <div class="stat abs" style="left:184px;width:156px"><p class="label">Leads Delivered Per Month</p><p class="value">Ticker 25,000+</p></div>
    <div class="stat abs" style="left:340px;width:176px"><p class="label">Countries We Can Reach</p><p class="value">Ticker to 50+</p></div>
  </section>

  <footer>
    <div class="footer-mark abs"></div>
    <p class="footer-about abs">Brightfold Reach can deliver high quality sales leads from any country in the world. This can include leads via email or telemarketing, account-based targeting (ABM) or identifying need and pain points through BANT / SQL campaigns.</p>
    <ul class="footer-nav abs"><li>Home</li><li>About Us</li><li>Our Services</li><li>Prospero &amp; QA</li><li>Technology</li><li>Intent Data</li><li>Testimonials</li><li>Contact Us</li></ul>
    <div class="footer-contact abs">
      <h5>Get in touch</h5>
      <p>000-123-4567</p>
      <p style="margin-top:3px">info@brightfoldreach-example.com</p>
      <p style="margin-top:3px"><b>London:</b> street address here,<br>London, 1234</p>
    </div>
    <p class="copyright abs">Copyright © 2020 brightfoldreach-example.com</p>
  </footer>

</main>
</div>
</body>
</html>
```